Software development and consultancy website

Company – Corvalto Limited , London, UK
Profile – we are providing integration solutions development / consultancy services for QEV integration projects across UK.
Our name refers two words - integration and grace - and it shows our clients our main specialization field and key characteristics of our solutions / products. We also would like to be associated with follow words: smart, reliable, unique.
The target audience is experienced IT professionals and managers.
Website look and feel should be professional and sophisticated, simple and elegant. I like minimalistic themes with no real object/people photos. Try to avoid messy/cluttered/colourful content. White dominating background is a must, don’t like dark websites.
I would prefer light, web 2.0 style colours, follow are in my main interest:
- combination of light grey and orange
- Logo colours
In terms of deliverables, theme should be coded and be ready to be placed to my test website. I would also suggest if you could create skin for Lantern theme. NOTE: Please make a quote excluding Lantern theme cost.
Attached are examples of logo and corporate stationery design and mockups of website with landing page layout and content page layout. Website design should not copy stationery design but to be consistent with.
Sites I like :
http://www.mailbrindle.example/
http://www.vorpex.example/
http://www.feltmark.example/tracelens/
http://www.deskorbit.example/
I changed project type to Context and increased the budget. Please refer project description for details

```html
<!DOCTYPE html>
<html lang="en">
<head>
<meta charset="utf-8">
<title>Corvalto Limited – Integration Solutions</title>
<style>
:root{
  --ink:#333333;
  --ink-soft:#555555;
  --orange:#e8790c;
  --green:#6a9e1f;
  --blue:#1e7fb8;
  --sky:#14b4f0;
  --white:#ffffff;
  --footer-text:#e8e8e8;
}
*{box-sizing:border-box;margin:0;padding:0}
html,body{width:1038px;height:1200px;overflow:hidden;background:var(--white)}
body{font-family:"PT Sans","Segoe UI",Arial,sans-serif;color:var(--ink)}
.canvas{position:relative;width:1038px;height:1200px;overflow:hidden;background:var(--white)}

/* brand */
.brand{position:absolute;left:29px;top:36px;display:flex;align-items:center;gap:12px}
.brand-dot{width:44px;height:44px;border-radius:50%;background:var(--orange)}
.brand-name{font-size:46px;font-weight:700;color:var(--ink-soft);letter-spacing:.5px;line-height:1}

/* navigation */
.main-nav{position:absolute;left:457px;top:35px;width:569px;height:40px;border-radius:12px;
  background:linear-gradient(#ffffff,#ececec);border:1px solid #dcdcdc;box-shadow:0 2px 3px rgba(0,0,0,.12)}
.main-nav a{position:absolute;top:10px;font-size:14px;color:#555;text-decoration:none;transform:translateX(-50%)}
.main-nav a.active{top:5px;padding:4px 10px;border-radius:9px;color:#fff;
  background:linear-gradient(#3fa4dd,#1770ad);box-shadow:0 0 0 2px #cfe7f5}

/* slider */
.slider{position:absolute;left:28px;top:117px;width:688px;height:317px;background:#fff;
  border:1px solid #e0e0e0;box-shadow:0 1px 4px rgba(0,0,0,.15);padding:5px}
.slider-stage{position:relative;width:100%;height:100%;background:linear-gradient(#18c0f6,#0fa6e6 70%,#3cbff0)}
.slider-shadow{position:absolute;left:78px;top:432px;width:580px;height:32px;border-radius:50%;
  background:radial-gradient(ellipse at center,rgba(0,0,0,.45),rgba(0,0,0,0) 70%)}
.slide-preview{position:absolute;left:60px;top:45px;width:290px;height:206px;border-radius:4px;
  background:linear-gradient(#e9f5fb,#d7ecf6);border:6px solid #6fd0f7}
.slide-features{position:absolute;left:390px;top:58px;color:#fff}
.slide-features h2{font-size:25px;font-weight:700;color:#1a3d5a;margin-bottom:8px}
.slide-features li{list-style:none;font-size:14px;line-height:22.5px;text-shadow:0 1px 1px rgba(0,0,0,.2)}
.slide-mascot{position:absolute;left:543px;top:184px;width:100px;height:100px;border-radius:50%;
  background:radial-gradient(circle at 40% 35%,#6fc6ff,#1460c8 75%)}
.slide-dots{position:absolute;left:278px;bottom:0;width:122px;height:26px;background:#fff;
  border-radius:5px 5px 0 0;display:flex;justify-content:center;align-items:center;gap:7px}
.slide-dots span{width:10px;height:10px;border-radius:50%;background:#1c6fa8}
.slide-dots span.current{background:#cfd8de}
.slider-arrow{position:absolute;top:252px;width:36px;height:54px}
.slider-arrow.prev{left:20px}
.slider-arrow.next{left:690px}

/* sidebar */
.promo{position:absolute;left:731px;top:117px;width:297px;height:317px;background:#fff;
  border:1px solid #e0e0e0;box-shadow:0 1px 4px rgba(0,0,0,.15);padding:5px}
.promo-inner{position:relative;width:100%;height:100%;background:var(--sky)}
.promo-title{position:absolute;left:20px;top:6px;font-size:24px;font-weight:400;line-height:29px;color:#1b1b1b}
.promo-card{position:absolute;left:6px;width:270px;height:61px;border-radius:8px;
  background:linear-gradient(#ffffff,#e6eef3);box-shadow:0 1px 2px rgba(0,0,0,.2)}
.promo-icon{position:absolute;left:10px;top:9px;width:46px;height:44px;border-radius:6px}
.promo-card h3{position:absolute;left:68px;top:5px;font-size:27px;font-weight:400;line-height:30px;white-space:nowrap}
.promo-card p{position:absolute;left:70px;top:37px;font-size:11px;color:#222;white-space:nowrap}
.card-tools{top:79px}.card-tools h3{color:var(--green)}.card-tools .promo-icon{background:linear-gradient(#a9c98a,#6d8e55)}
.card-ideas{top:148px}.card-ideas h3{color:var(--blue)}.card-ideas .promo-icon{background:linear-gradient(#9fd0f5,#2f6db5)}
.card-done{top:216px}.card-done h3{color:var(--orange)}.card-done .promo-icon{background:linear-gradient(#ffd36e,#f08a14)}
.promo-note{position:absolute;left:0;right:0;top:285px;text-align:center;font-size:11px;color:#fff}

/* about */
.about{position:absolute;left:29px;top:472px;width:983px}
.about h1{font-size:23px;font-weight:400;color:var(--orange);line-height:28px}
.about-photo{float:right;width:271px;height:236px;margin:22px 0 10px 25px;
  background:linear-gradient(135deg,#3a3a3a,#d9dadb 55%,#f2f2f2);border:1px solid #ccc}
.about h2{font-size:16px;font-weight:400;color:#555;margin-top:14px;line-height:20px}
.about-body{margin-top:12px}
.about p{font-size:12.3px;line-height:24.9px;color:#333;margin-bottom:24.9px}

/* footer */
.site-footer{position:absolute;left:0;top:1035px;width:1038px;height:165px;
  background:linear-gradient(#222,#0f0f0f);border-top:1px solid #444;color:var(--footer-text);font-size:11.5px}
.footer-divider{position:absolute;top:32px;width:1px;height:100px;background:#3b3b3b}
.company{position:absolute;left:29px;top:31px;line-height:15px}
.company .indent{padding-left:106px}
.company .reg{margin-top:14px}
.legal{position:absolute;left:360px;width:390px;top:26px;text-align:center}
.legal nav span{padding:0 6px}
.legal .copy{margin-top:16px}
.legal .small{margin-top:7px;font-size:10.5px;line-height:13px;padding:0 20px}
.social{position:absolute;left:819px;top:24px}
.social-row{display:flex;align-items:center;height:36px}
.social-row .label{width:76px}
.social-row + .social-row{margin-top:10px}
.badge{width:34px;height:34px;border-radius:50%;margin-right:5px}
.badge.b1{background:#2a5cad}.badge.b2{background:#48b8e8}.badge.b3{background:#2189c2}.badge.b4{background:#f07a1e}
</style>
</head>
<body>
<div class="canvas">

  <header>
    <div class="brand"><span class="brand-dot"></span><span class="brand-name">corvalto</span></div>
    <nav class="main-nav">
      <a href="#" style="left:70px">Home</a>
      <a href="#" style="left:171px">About Us</a>
      <a href="#" class="active" style="left:273px">Products</a>
      <a href="#" style="left:379px">Services</a>
      <a href="#" style="left:480px">Blog</a>
    </nav>
  </header>

  <div class="slider-shadow"></div>
  <section class="slider">
    <div class="slider-stage">
      <div class="slide-preview" role="img" aria-label="Preview of an under-construction page template with countdown and download button"></div>
      <div class="slide-features">
        <h2>Features</h2>
        <ul>
          <li>- Fully Customizable</li>
          <li>- Easy to modify &amp; Change colors</li>
          <li>- Well organized .psd files</li>
          <li>- Grouped Layers</li>
          <li>- Labelled Layers</li>
        </ul>
      </div>
      <div class="slide-mascot" role="img" aria-label="Cheerful blue mascot character"></div>
      <div class="slide-dots"><span></span><span></span><span class="current"></span><span></span><span></span></div>
    </div>
  </section>
  <svg class="slider-arrow prev" viewBox="0 0 36 54" aria-hidden="true"><path d="M28 6 L8 27 L28 48" fill="none" stroke="#555" stroke-width="9" stroke-linecap="round" stroke-linejoin="round"/><path d="M28 6 L8 27 L28 48" fill="none" stroke="#9a9a9a" stroke-width="4" stroke-linecap="round" stroke-linejoin="round"/></svg>
  <svg class="slider-arrow next" viewBox="0 0 36 54" aria-hidden="true"><path d="M8 6 L28 27 L8 48" fill="none" stroke="#555" stroke-width="9" stroke-linecap="round" stroke-linejoin="round"/><path d="M8 6 L28 27 L8 48" fill="none" stroke="#9a9a9a" stroke-width="4" stroke-linecap="round" stroke-linejoin="round"/></svg>

  <aside class="promo">
    <div class="promo-inner">
      <h2 class="promo-title">How to make a Perfect<br>QEV PI Project</h2>
      <div class="promo-card card-tools"><div class="promo-icon" role="img" aria-label="Tools window icon"></div><h3>Get Nice Tools !</h3><p>Designed by developers for developers</p></div>
      <div class="promo-card card-ideas"><div class="promo-icon" role="img" aria-label="Light bulb icon"></div><h3>Get Right Ideas !</h3><p>Check it out on our Blogs</p></div>
      <div class="promo-card card-done"><div class="promo-icon" role="img" aria-label="Project folder icon"></div><h3>Get It Done !</h3><p>Hire* us on short or long term project</p></div>
      <p class="promo-note">*UK Projects only. Sorry all the rest of the world.</p>
    </div>
  </aside>

  <section class="about">
    <h1>About Us</h1>
    <div class="about-photo" role="img" aria-label="Photo of a team working together at a laptop"></div>
    <h2>What we Do ?</h2>
    <div class="about-body">
      <p>Lorem Ipsum is simply dummy text of the printing and typesetting industry. Lorem Ipsum has been the industry's standard dummy text ever since the 1500s, when an unknown printer took a galley of type and scrambled it to make a type specimen book. It has survived not only five centuries, but also the leap into electronic typesetting, remaining essentially unchanged. It was popularised in the 1960s with the release of Lettrafix sheets containing Lorem Ipsum passages, and more recently with desktop publishing software like Pagewright Studio including versions of Lorem Ipsum.</p>
      <p style="margin-bottom:0">It is a long established fact that a reader will be distracted by the readable content of a page when looking at its layout. The point of using Lorem Ipsum is that it has a more-or-less normal distribution of letters, as opposed to using 'Content here, content here', making it look like readable English. Many desktop publishing packages and web page editors now use Lorem Ipsum as their default model text,</p>
      <p>'lorem ipsum' will uncover many web sites still in their infancy. Various versions have evolved over the years, sometimes by accident, sometimes on purpose (injected humour and the like). making it look like readable English. Many desktop publishing packages and web page editors now use Lorem Ipsum as their default model text, and a search for Lorem Ipsum is simply dummy text of the printing and typesetting industry. Lorem Ipsum has been the industry's standard dummy text ever since the 1500s, when an unknown printer took a galley of type and scrambled it to make a type specimen book. It has survived not only five centuries, but also the leap into electronic typesetting, remaining essentially unchanged.</p>
      <p>It was popularised in the 1960s with the release of Lettrafix sheets containing Lorem Ipsum passages, and more recently with desktop publishing software like Pagewright Studio including versions of Lorem Ipsum.</p>
    </div>
  </section>

  <footer class="site-footer">
    <div class="company">
      <div>Corvalto Limited</div>
      <div>Registered address : 48 Quillby House,</div>
      <div class="indent">212 Marlow Lane,</div>
      <div class="indent">London, SE 4QT, United Kingdom</div>
      <div class="reg">Company Registration No :</div>
      <div class="indent" style="padding-left:100px">708214 (England and Wales)</div>
    </div>
    <span class="footer-divider" style="left:342px"></span>
    <div class="legal">
      <nav>Website Disclaimer<span>|</span>Terms and Conditions<span>|</span>Privacy Policy</nav>
      <p class="copy">Copyright @ 2011 www.corvaltolimited.example</p>
      <p class="small">Sections 1.10.32 and 1.10.33 from the Quillmere Codex are also reproduced in their exact original form, accompanied by English versions from the 1914 translation by J. Wetherby.</p>
    </div>
    <span class="footer-divider" style="left:768px"></span>
    <div class="social">
      <div class="social-row"><span class="label">Follow us on :</span><span class="badge b1"></span><span class="badge b2"></span><span class="badge b3"></span></div>
      <div class="social-row"><span class="label">Subscribe :</span><span class="badge b4"></span></div>
    </div>
  </footer>

</div>
</body>
</html>
```